Design for Cards used in Corporate Leadership and Communications Card Game

Background:
Grounded Pathways is an organizational development consulting firm that helps organizations improve leadership, communications, and team work through simple and easy methods. We believe that the systems and methods commonly used in companies are overly complex and contrary to what people do intuitively. Our methods work with what people do naturally and innately. Our brand conveys simplicity and ease of use. We often use just black and white with a touch of color in our look and feel along with Zen imagery. Our tag line is "Quiet steps, lasting change."
Purpose of project:
This project is a card game used in corporate settings to improve leadership and communications skills. The cards portray a successful leader with their bios, values, and behaviors.
The cards are 4 by 6 inches, color, and two-sided, with a picture and text on the front and just text on the back. The game is a work in progress so it is important that we can use the design template to create more cards. Our preference is Microsoft Word or Powerpoint. The source files attached are in Word.
Desired look:
The look and feel we want to create is clean, clear, simple, easy to read, and down to earth with a zen feel optional. We would like to have our logo somewhere on the card. They need to appeal to a professional audience.
Summary of requirements:
• 4x6 inch playing cards depicting bios
• Color, double-sided
• Instruction card is all text
• Includes Grounded Pathways logo
• Must be able to edit design template for future use
• Word or Powerpoint template
• Desired look and feel: professional, clear, easy-to-read, down-to-earth, perhaps zen
Files attached:
• 5 cards including instruction card
• Logo image
. Company business card just for reference
Updates

Project Deadline Extended
Reason: Give people more time.

Please note that the business card was included for reference only so you could see our current look and feel. The logo file is Grounded Pathways. Please do not include the business card in your design, just the Grounded Pathways logo.

Target Market(s)

The target market is business and professional managers who desire a creative and fun way to improve the team working and communication skills of their employees.

Industry/Entity Type

Communications

Requirements
Must have
• Must fit in 4X 6 format in either Word or Powerpoint. Must be very easy to read and clean feel.
Nice to have
• Zen feel
Should not have
• Lots of color, modern look, hard to read font

PLEASE NOTE: Business card was included for reference only. Should not be part of design.

```html
<!DOCTYPE html>
<html lang="en">
<head>
<meta charset="utf-8">
<title>Grounded Pathways – Card Instructions</title>
<link href="https://fonts.googleapis.com/css2?family=Lora:wght@400;700&family=Mulish:wght@400;600&display=swap" rel="stylesheet">
<style>
  :root {
    --paper: #ffffff;
    --ink: #2b2b2b;
    --frame: #dba592;
    --rule: #d9d9d9;
    --brand: #555555;
  }
  html, body {
    margin: 0;
    padding: 0;
    width: 1200px;
    height: 900px;
    overflow: hidden;
    background: var(--paper);
  }
  .sheet {
    position: relative;
    width: 1200px;
    height: 900px;
    background: var(--paper);
    color: var(--ink);
    font-family: "Mulish", Arial, sans-serif;
    font-size: 16px;
    line-height: 1.24;
  }
  .fold-line {
    position: absolute;
    left: 600px;
    top: 0;
    width: 1px;
    height: 900px;
    background: var(--rule);
  }
  .panel {
    position: absolute;
    box-sizing: border-box;
    border: 1.5px solid var(--frame);
    padding: 14px 18px;
    overflow: hidden;
  }
  .panel--usage { left: 19px; top: 19px; width: 560px; height: 864px; }
  .panel--team { left: 621px; top: 19px; width: 560px; height: 626px; padding-top: 26px; }
  .panel--expect { left: 621px; top: 665px; width: 560px; height: 218px; padding-top: 22px; }

  .brand {
    display: flex;
    align-items: center;
    justify-content: center;
    gap: 12px;
    margin: 22px 0 26px;
  }
  .brand__mark {
    width: 30px;
    height: 30px;
    border-radius: 50%;
    background: var(--brand);
  }
  .brand__name {
    font-family: "Lora", Georgia, serif;
    font-weight: 700;
    font-size: 34px;
    color: var(--brand);
  }
  h2 {
    font-family: "Lora", Georgia, serif;
    font-weight: 700;
    font-size: 21px;
    text-align: center;
    margin: 0 0 16px;
  }
  h3 {
    font-family: "Lora", Georgia, serif;
    font-weight: 700;
    font-size: 21px;
    margin: 14px 0 10px;
  }
  p { margin: 0 0 6px; }
  ul { margin: 0; padding-left: 22px; }
  ol { margin: 0; padding: 0; list-style: none; }
  ol li { margin-bottom: 14px; }
  .lead-in {
    font-family: "Lora", Georgia, serif;
    font-weight: 700;
    font-size: 20px;
  }
  .justified { text-align: justify; }
  .gap { margin-top: 22px; }
  .panel--team h2 { margin: 26px 0 26px; }
</style>
</head>
<body>
<div class="sheet">
  <div class="fold-line"></div>

  <section class="panel panel--usage">
    <div class="brand">
      <span class="brand__mark"></span>
      <span class="brand__name">Grounded Pathways</span>
    </div>
    <h2>Instructions for using the cards</h2>
    <p>The role-playing cards can be used in a number of applications whenever there is a need to:</p>
    <ul>
      <li>Depersonalize feedback</li>
      <li>Expand perspectives and adopt new behaviors</li>
      <li>Clarify expectations regarding behaviors</li>
    </ul>
    <p>One-on-one Feedback (project, progress, or performance reviews)</p>
    <p>The goal is to depersonalize the feedback, make both parties provide feedback together, and use more than one perspective.</p>
    <h3>Instructions:</h3>
    <ol>
      <li>1.&nbsp; Each person prepares by choosing a card to voice a managerial perspective they want the other to hear and noting some points of feedback.</li>
      <li>2. During the meeting, one person shows the card and both provide feedback in that persona and agree on key, relevant points.</li>
      <li>3. Repeat Step 2 using the second person’s chosen card.</li>
      <li>4. Both compare and contrast the feedback for lessons going forward.&nbsp; If stalemate or otherwise desired, they choose a third card and both perform the feedback again.</li>
    </ol>
    <h2>Meeting or team feedback</h2>
    <p>The goal is to depersonalize feedback, gain perspective, and make it fun to do at the end of each meeting.</p>
    <p><span class="lead-in">Instructions:</span> At the end of the meeting, each participant, including the meeting leader, chooses a card on purpose or at random, and takes turns providing feedback in the persona of the leader.</p>
  </section>

  <section class="panel panel--team">
    <p>Depending on the time allotted for feedback, you can limit the amount of feedback from each leader/ participant. Alternately, the meeting leader can choose cards at random and ask participants for feedback in that persona.&nbsp; The meeting leader or team can determine which feedback to incorporate for next meeting.</p>
    <h2>Team Development and Innovation</h2>
    <p>The goal is to create awareness of missing skills and traits on the team and use the personas to fill those and to improve creativity by using other’s perspectives.</p>
    <p class="justified gap"><span class="lead-in">Instructions:</span> Review the cards to determine which personas the team needs but is lacking.&nbsp; Create virtual seats for these leaders and assign team members the responsibilities for representing these perspectives.&nbsp; During brainstorming, choose cards at random and generate ideas as the personas. Alternately, team members can act as the leader personas during the meetings.Expectations Setting (at the start of a project,initiative, team or relationship) The goal is to clarify the expected behaviors at the outset. Each person chooses three cards: one that best represents him; one that she would like work with or is needed for the project; and one she least would like to work with. Each discusses his picks and agrees to actions for working together.</p>
  </section>

  <section class="panel panel--expect">
    <p><span class="lead-in">Expectations Setting</span> (at the start of a project, initiative, team or relationship)</p>
    <p>The goal is to clarify the expected behaviors at the outset.</p>
    <p class="justified gap">Each person chooses three cards: one that best represents him; one that she would like work with or is needed for the project; and one she least would like to work with.&nbsp; Each discusses his picks and agrees to actions for working together</p>
  </section>
</div>
</body>
</html>
```